We are a rubber stamp manufacturer that has been in business since 1945. We are looking for something that says "quality products since 1945". This is to be used in our new catalogue next to our logo, but not as part of the logo. It can be a seal, sticker, banner... just want to be able to put it on our website and in print media. It has to be vector art made in illustrator with the fonts and all working files included. Our website is http://www.quillmarsh.ca/ and company logo is Red, White, and Black so I think we should stick to shades of those colours... but isn't a must. We had started to work on something (attached) but just didn't love it.

```html
<!DOCTYPE html>
<html lang="en">
<head>
<meta charset="utf-8">
<title>Quality Products Since 1945 Banner</title>
<link rel="stylesheet" href="https://fonts.googleapis.com/css2?family=Courier+Prime:wght@700&display=swap">
<style>
  :root {
    --page: #ffffff;
    --tread-red: #d8261f;
    --tread-red-deep: #c01d17;
    --tread-light: #e6e2e0;
    --ink-strong: #1c1a1a;
    --ink-mid: #3a3535;
    --ink-soft: #5a5252;
  }
  html, body {
    margin: 0;
    padding: 0;
    width: 1185px;
    height: 1200px;
    overflow: hidden;
    background: var(--page);
  }
  .canvas {
    display: block;
    width: 1185px;
    height: 1200px;
  }
  .banner-shadow {
    filter: drop-shadow(6px 8px 10px rgba(0, 0, 0, 0.35));
  }
  .tagline {
    font-family: "Courier Prime", "Courier New", monospace;
    font-weight: 700;
    font-size: 72px;
  }
  .tagline--front { fill: var(--ink-strong); }
  .tagline--middle { fill: var(--ink-mid); opacity: 0.85; }
  .tagline--back { fill: var(--ink-soft); opacity: 0.7; }
</style>
</head>
<body>
<svg class="canvas" viewBox="0 0 1185 1200" xmlns="http://www.w3.org/2000/svg">
  <defs>
    <linearGradient id="tread-tone" x1="0" y1="0" x2="0" y2="1">
      <stop offset="0" stop-color="var(--tread-red)"/>
      <stop offset="0.5" stop-color="var(--tread-red-deep)"/>
      <stop offset="1" stop-color="var(--tread-red)"/>
    </linearGradient>
    <clipPath id="banner-edge">
      <rect x="-640" y="-165" width="1280" height="330"/>
    </clipPath>
  </defs>

  <g class="banner" transform="translate(596 600) rotate(-44)">
    <g class="banner-shadow">
      <rect class="banner-tread" x="-640" y="-165" width="1280" height="330"
            fill="url(#tread-tone)" role="img"
            aria-label="Red tyre tread pattern with light grey grooves"/>
    </g>
    <g class="banner-lines" clip-path="url(#banner-edge)">
      <rect class="tread-groove" x="-640" y="-58" width="1280" height="6" fill="var(--tread-light)"/>
      <rect class="tread-groove" x="-640" y="52" width="1280" height="6" fill="var(--tread-light)"/>
      <text class="tagline tagline--front" x="-620" y="-88"
            textLength="1220" lengthAdjust="spacingAndGlyphs">quality products since 1945</text>
      <text class="tagline tagline--middle" x="-600" y="22"
            textLength="1205" lengthAdjust="spacingAndGlyphs">quality products since 1945</text>
      <text class="tagline tagline--back" x="-585" y="132"
            textLength="1195" lengthAdjust="spacingAndGlyphs">quality products since 1945</text>
    </g>
  </g>
</svg>
</body>
</html>
```